PLUMBING POSTCARD DESIGN (MARKETING)

We are a local Plumbing business , Needing a post card to market domestic plumbing maintenance in my local area. The post card will have a magnet business card attached so allowance in design will need to be made. I have a slogan i want Incorporated into the design and is "TRY THE BEST, FLUSH THE REST"
I have attached my company name and logo to also incorporate into the design.
post card size 21cm L x 10cm H
business magnet card that will be attached to post card is 9cm L X 5.5cm H.
Post card will be one sided and will need following text inserted into design:
Pipewell would like to offer its fellow locals $40 off their next plumbing job. We pride ourselves in supplying the highest level of workmanship at the most competitive prices. CALL US TODAY
0431 582 907
Target Market(s)
Property owners (domestic market0
Industry/Entity Type
Plumbing
Requirements
Must have
- Eye catching, Slogan, company name and logo

```html
<!DOCTYPE html>
<html lang="en">
<head>
<meta charset="utf-8">
<title>Pipewell – Postcard</title>
<link href="https://fonts.googleapis.com/css2?family=Anton&family=Nunito:wght@700;800&display=swap" rel="stylesheet">
<style>
  :root{
    --sky:#12aad8;
    --sky-deep:#2190c6;
    --orange:#f0763a;
    --orange-light:#f39a3a;
    --yellow:#f6bb3c;
    --white:#ffffff;
    --ink:#555a60;
    --silver-hi:#f2f3f5;
    --silver-lo:#9ea3a9;
  }
  *{margin:0;padding:0;box-sizing:border-box}
  html,body{width:1200px;height:571px;overflow:hidden;background:var(--white)}
  .postcard{position:relative;width:1200px;height:571px;overflow:hidden;background:var(--white);font-family:"Nunito",sans-serif}
  .backdrop{position:absolute;inset:0}
  .slogan{position:absolute;top:36px;left:0;width:1200px;text-align:center;font-family:"Anton",sans-serif;font-size:70px;line-height:1;color:var(--white);letter-spacing:0.5px}
  .van-photo{position:absolute;border-radius:22px 60px 30px 16px;background:linear-gradient(180deg,var(--silver-hi) 0%,#d6d9dd 55%,var(--silver-lo) 80%,#4b4f55 100%)}
  .van-photo--main{left:63px;top:210px;width:537px;height:208px}
  .van-photo--mini{left:265px;top:71px;width:237px;height:87px;border-radius:10px 26px 12px 8px}
  .van-brand{position:absolute;display:flex;align-items:center;gap:8px;color:var(--ink);font-weight:700}
  .van-brand__dot{width:34px;height:34px;border-radius:50%;background:var(--sky)}
  .van-brand--main{left:95px;top:240px;font-size:38px;letter-spacing:1px}
  .van-tagline{position:absolute;left:152px;top:278px;font-size:17px;font-weight:700;color:var(--ink);letter-spacing:0.5px}
  .van-brand--mini{left:12px;top:6px;font-size:15px;gap:4px}
  .van-brand--mini .van-brand__dot{width:14px;height:14px}
  .cta-left{position:absolute;left:63px;top:432px;width:420px}
  .cta-left__label{margin-left:126px;font-family:"Anton",sans-serif;font-size:27px;color:var(--orange);line-height:1}
  .cta-left__phone{display:flex;align-items:center;gap:10px;margin-top:14px;font-family:"Anton",sans-serif;font-size:66px;line-height:1;color:var(--orange)}
  .phone-icon{fill:currentColor;flex:none}
  .offer-card{position:absolute;left:638px;top:211px;width:514px;height:314px;border-radius:26px;overflow:hidden;box-shadow:0 6px 16px rgba(0,0,0,.28)}
  .offer-card__shapes{position:absolute;inset:0}
  .offer{position:absolute;left:56px;top:36px;color:var(--white);font-family:"Anton",sans-serif}
  .offer__amount{font-size:64px;line-height:1}
  .offer__text{margin-top:4px;font-size:22px;line-height:26px}
  .offer-card__pitch{position:absolute;left:232px;top:166px;width:275px;font-size:14.5px;line-height:16.5px;color:var(--ink);font-weight:800}
  .offer-card__cta{position:absolute;left:134px;top:252px;display:flex;align-items:center;color:var(--white);font-family:"Anton",sans-serif}
  .offer-card__label{font-size:14px;margin-right:20px;margin-top:10px}
  .offer-card__phone{display:flex;align-items:center;gap:4px;font-size:38px;line-height:1}
</style>
</head>
<body>
<main class="postcard">
  <svg class="backdrop" viewBox="0 0 1200 571" width="1200" height="571" aria-hidden="true">
    <defs>
      <linearGradient id="warm" x1="0" y1="0" x2="1" y2="0">
        <stop offset="0" stop-color="var(--orange)"/>
        <stop offset="0.6" stop-color="var(--orange-light)"/>
        <stop offset="1" stop-color="var(--yellow)"/>
      </linearGradient>
      <linearGradient id="sky" x1="0" y1="0" x2="1" y2="1">
        <stop offset="0" stop-color="var(--sky)"/>
        <stop offset="1" stop-color="var(--sky-deep)"/>
      </linearGradient>
    </defs>
    <path d="M330 571 C500 545 610 480 660 400 L810 190 C950 180 1100 200 1200 228 L1200 571 Z" fill="url(#warm)"/>
    <path d="M0 0 H1200 V228 C1000 195 760 168 520 158 C320 150 120 140 0 141 Z" fill="url(#sky)"/>
  </svg>

  <h1 class="slogan">TRY THE BEST, FLUSH THE REST</h1>

  <div class="van-photo van-photo--main" role="img" aria-label="Photo of a silver company van with the Pipewell name on its side"></div>
  <div class="van-brand van-brand--main"><span class="van-brand__dot"></span>PIPEWELL</div>
  <div class="van-tagline">PLUMBING | DRAINAGE | GAS</div>

  <div class="cta-left">
    <p class="cta-left__label">CALL US TODAY</p>
    <p class="cta-left__phone">
      <svg class="phone-icon" width="40" height="40" viewBox="0 0 24 24" aria-hidden="true"><path d="M6.6 10.8c1.4 2.8 3.8 5.1 6.6 6.6l2.2-2.2c.3-.3.7-.4 1-.2 1.1.4 2.3.6 3.6.6.6 0 1 .4 1 1V20c0 .6-.4 1-1 1C10.6 21 3 13.4 3 4c0-.6.4-1 1-1h3.5c.6 0 1 .4 1 1 0 1.3.2 2.5.6 3.6.1.3 0 .7-.2 1l-2.3 2.2z"/></svg>
      0431 582 907
    </p>
  </div>

  <section class="offer-card">
    <svg class="offer-card__shapes" viewBox="0 0 514 314" width="514" height="314" aria-hidden="true">
      <defs>
        <linearGradient id="cardWarm" x1="0" y1="0" x2="1" y2="0">
          <stop offset="0" stop-color="var(--orange-light)"/>
          <stop offset="1" stop-color="var(--orange)"/>
        </linearGradient>
      </defs>
      <rect width="514" height="314" fill="var(--white)"/>
      <path d="M0 248 Q280 222 514 212 V314 H0 Z" fill="url(#sky)"/>
      <path d="M0 0 H298 Q200 190 76 314 H0 Z" fill="var(--yellow)"/>
      <path d="M0 0 H282 Q190 185 54 314 H0 Z" fill="url(#cardWarm)"/>
    </svg>

    <div class="offer">
      <p class="offer__amount">$40</p>
      <p class="offer__text">OFF YOUR<br>NEXT<br>PLUMBING<br>JOB</p>
    </div>

    <div class="van-photo van-photo--mini" role="img" aria-label="Photo of the silver Pipewell company van">
      <div class="van-brand van-brand--mini"><span class="van-brand__dot"></span>PIPEWELL</div>
    </div>

    <p class="offer-card__pitch">We pride ourselves in supplying the highest level of workmanship at the most competitive prices.</p>

    <div class="offer-card__cta">
      <span class="offer-card__label">CALL US TODAY</span>
      <span class="offer-card__phone">
        <svg class="phone-icon" width="22" height="22" viewBox="0 0 24 24" aria-hidden="true"><path d="M6.6 10.8c1.4 2.8 3.8 5.1 6.6 6.6l2.2-2.2c.3-.3.7-.4 1-.2 1.1.4 2.3.6 3.6.6.6 0 1 .4 1 1V20c0 .6-.4 1-1 1C10.6 21 3 13.4 3 4c0-.6.4-1 1-1h3.5c.6 0 1 .4 1 1 0 1.3.2 2.5.6 3.6.1.3 0 .7-.2 1l-2.3 2.2z"/></svg>
        0431 582 907
      </span>
    </div>
  </section>
</main>
</body>
</html>
```